Flyer, poster, banner and social media titles designs for Community Renewal Guidlines

The Shared Guidelines for Community Renewal provide a nationally agreed framework to guide recovery policy and practice across Australia. The Principles support recovery practitioners, governments, non-government organisations and communities to deliver effective, community-centred recovery outcomes.
The Principles have recently been refreshed through extensive consultation and we require a contemporary visual identity and design suite that will increase awareness, engagement and practical application of the Principles.
The redesign will cover:
• A4 Brochure (primary publication)
• A3 Poster
• Pull up banner
• Social Media Tiles
The new design should:
• Create a recognisable brand for the Shared Guidelines.
• Appeal to both experienced and emerging recovery practitioners.
• Reflect contemporary disaster recovery practice.
• Feel people-focused rather than government-focused.
• Support future resources such as videos, implementation guides, presentations and workshop materials.
• Remain relevant for several years without requiring a major redesign.
Target Audience
• Disaster recovery practitioners
• Government agencies
• Non-government organisations
• Community recovery workers
• Recovery managers and leaders
• Community stakeholders and volunteers
The visual identity should reflect the six Principles:
• Understanding Context
• Recognising Complexity
• Community-Centred Approaches
• Coordination
• Communication
• Capacity Building
The design should communicate:
• Recovery is centred on people and communities.
• Recovery is collaborative and involves many sectors.
• Recovery is adaptive, inclusive and evidence-informed.
• Recovery supports resilience and long-term wellbeing.
• The Principles provide practical guidance for recovery practice.
We are looking for:
• Modern and professional
• Warm and approachable
• Human-centred
• Inclusive and accessible
• Australian in context
• Visually engaging
• Suitable for print and digital use
We would like to avoid:
• Images of disaster destruction
• Emergency response imagery (fire trucks, flashing lights, etc.)
• Overly corporate or bureaucratic designs
• Designs that focus on deficits rather than recovery and growth
Consider themes such as:
• Connection and collaboration
• Communities and people
• Growth, recovery and renewal
Accessibility
Designs should:
• Meet accessibility best practice
• Use clear typography
• Achieve strong colour contrast
• Be suitable for both digital and print formats

Deliverables
1. Principles Brochure
• A4 trifold size x 2 (online and print friendly version)
• A side to include cover side, logos side and overview of principles.
• B side full details of the principles
• Graphic to highlight the 3 c’s concept (RECOVERY Context, complexity, community centred, coordinate, communicate and capacity). Currently 3 circles.
• Can be printed and distributed electronically
2. Poster
• A1 and A3 versions
• Suitable for office and workshop display
3. Pull-Up Banner - 850 mm (W) × 2000 mm (H)
• Conference and event use
• High visual impact
• Strong branding and concise messaging
4. Social Media Tiles x 3
Updates

We are providing an extension and increasing the budget following feedback from designers. We are wanting the resources to look and feel different from the existing designs, considering either a different colour palette in the designs or different motif with the leave design. Any nature based designs should consider the Australian fauna or flora. Also suggest avoiding images in the designs. The principles are not numbered or liner in the concept of how they function. Happy to answer any further questions and thank you for your suggested concepts.

Target Market(s)

Disaster recovery practitioners, Government agencies , Non-government organisations, Community recovery workers and Community stakeholders and volunteers

Industry/Entity Type

Disaster recovery

Colors

Designer to choose colors to be used in the design.

Requirements
Must have
• Modern, warm, visually engaging, human-centred, Australian in context and different to the current design.
Nice to have
• Symbols for each principles
Should not have
• Images of disaster destruction, Emergency response imagery, Overly corporate or bureaucratic designs, Designs that focus on deficits rather than recovery and growth, avoid too much black

```html
<!DOCTYPE html>
<html lang="en">
<head>
<meta charset="utf-8">
<title>Shared Guidelines for Community Renewal – Brochure</title>
<link href="https://fonts.googleapis.com/css2?family=Montserrat:wght@500;600;700;800&family=Nunito+Sans:wght@400;600;700&display=swap" rel="stylesheet">
<style>
:root{
  --navy:#0c3b4b;
  --teal:#136b6e;
  --green:#7b9a3d;
  --green-light:#9db35a;
  --orange:#e0652f;
  --amber:#eea03a;
  --yellow:#d9a22c;
  --purple:#7a4f94;
  --cream:#f1efe7;
  --cream-2:#e8e6da;
  --ink:#23313a;
  --muted:#4a5660;
  --line:#c9c6b8;
}
*{box-sizing:border-box;margin:0;padding:0}
html,body{width:1200px;height:800px;overflow:hidden;background:#fff}
body{position:relative;font-family:"Nunito Sans",Arial,sans-serif;color:var(--ink)}
.panel{position:absolute}
.heading{font-family:"Montserrat",Arial,sans-serif;font-weight:700;letter-spacing:.02em}

/* outside spread */
.outside{position:absolute;left:11px;top:8px;width:1178px;height:386px}
.commitment{left:0;top:0;width:259px;height:386px;background:var(--navy);color:#fff}
.commitment .heading{position:absolute;left:37px;top:64px;font-size:11px;color:var(--amber)}
.commitment p{position:absolute;left:37px;top:84px;width:170px;font-size:8.6px;line-height:1.55}
.commitment .motto{top:142px;color:var(--green-light);font-weight:700;font-size:9.6px;line-height:1.5}
.commitment .art{position:absolute;left:0;top:180px;width:200px;height:206px;border-radius:0 60% 0 0;
  background:radial-gradient(ellipse at 40% 50%,rgba(157,179,90,.55),rgba(233,181,58,.25) 55%,rgba(12,59,75,0) 75%)}

.partners{left:259px;top:0;width:286px;height:386px;background:var(--cream);text-align:center}
.partners .heading{position:absolute;left:0;right:0;top:46px;font-size:8.6px;font-weight:600;letter-spacing:.14em}
.logo-grid{position:absolute;left:46px;top:68px;display:grid;grid-template-columns:repeat(3,61px);gap:5px;}
.logo-slot{height:38px;border:1px solid var(--line);background:#f6f4ee}
.partners .note{position:absolute;left:0;right:0;top:256px;font-size:8.6px;line-height:1.55}
.partners .rule{position:absolute;left:118px;top:298px;width:50px;height:1px;background:var(--green)}
.partners .learn{position:absolute;left:0;right:0;top:322px;font-size:10px;color:var(--green);font-weight:600}
.partners .url{position:absolute;left:0;right:0;top:337px;font-size:11px;font-weight:700}

.cover{left:545px;top:0;width:318px;height:386px;overflow:hidden;background:var(--navy)}
.cover svg{position:absolute;inset:0}
.cover .kicker{position:absolute;left:34px;top:58px;font-size:11.5px;color:var(--amber)}
.cover h1{position:absolute;left:32px;top:72px;font-family:"Montserrat",Arial,sans-serif;font-weight:800;font-size:41px;line-height:1.05;color:#fff;letter-spacing:-.01em}
.cover h1 span{display:block;color:var(--green-light)}
.cover .tagline{position:absolute;left:35px;top:218px;color:#fff;font-size:10px;line-height:1.45}

.overview{left:863px;top:0;width:315px;height:386px;background:var(--cream)}
.overview .heading{position:absolute;left:34px;top:37px;font-size:12px;line-height:1.3}
.overview p{position:absolute;left:34px;width:205px;font-size:8px;line-height:1.55}
.overview .people{position:absolute;left:38px;top:306px;width:70px;height:56px;border-radius:10px;
  background:linear-gradient(135deg,rgba(19,107,110,.25),rgba(238,160,58,.3),rgba(122,79,148,.25))}
.overview .pledge{position:absolute;left:143px;top:303px;width:160px;font-size:9.6px;font-weight:700;line-height:1.45;color:var(--ink)}
.overview .pledge em{font-style:normal;color:var(--green)}

/* inside spread */
.inside{position:absolute;left:11px;top:403px;width:1178px;height:387px;background:var(--cream);overflow:hidden}
.relationship{left:0;top:0;width:169px;height:343px;background:var(--cream-2)}
.relationship .heading{position:absolute;left:19px;top:20px;font-size:9.4px;line-height:1.35}
.relationship p{position:absolute;left:19px;width:140px;font-size:7px;line-height:1.55}
.venn{position:absolute;left:0;top:120px}

.principle{top:0;height:343px;border-left:1px solid #ddd9cc}
.principle .icon{position:absolute;left:50%;top:22px;margin-left:-24px;width:48px;height:48px;border-radius:50%}
.principle .icon::after{content:"";position:absolute;left:14px;top:14px;width:20px;height:20px;border:2px solid #fff;border-radius:50%}
.principle h2{position:absolute;left:0;right:0;top:82px;text-align:center;font-family:"Montserrat",Arial,sans-serif;font-weight:700;font-size:11px;line-height:1.25;letter-spacing:.02em}
.principle .lead{position:absolute;left:25px;right:18px;top:120px;font-size:7.2px;line-height:1.6}
.principle ul{position:absolute;left:25px;right:14px;top:178px;list-style:none}
.principle li{position:relative;padding-left:10px;font-size:6.4px;line-height:1.55;margin-bottom:6px}
.principle li::before{content:"";position:absolute;left:0;top:3px;width:4px;height:4px;border-radius:50%;background:var(--dot)}

.context{left:169px;width:170px;--dot:var(--green)} .context h2{color:var(--green)} .context .icon{background:var(--green)}
.complexity{left:339px;width:173px;--dot:var(--teal)} .complexity h2{color:var(--teal)} .complexity .icon{background:var(--navy)}
.community{left:512px;width:154px;--dot:var(--orange)} .community h2{color:var(--orange)} .community .icon{background:var(--orange)}
.coordination{left:666px;width:171px;--dot:var(--green)} .coordination h2{color:var(--green)} .coordination .icon{background:var(--green)}
.communication{left:837px;width:180px;--dot:var(--purple)} .communication h2{color:var(--purple)} .communication .icon{background:var(--purple)}
.capacity{left:1017px;width:161px;--dot:var(--yellow)} .capacity h2{color:var(--yellow)} .capacity .icon{background:var(--yellow)}

.waves{position:absolute;left:0;top:285px}
.footer-band{position:absolute;left:0;top:343px;width:1178px;height:44px;background:var(--navy);display:flex;align-items:center;padding:0 36px;font-size:8.4px;color:#fff}
.footer-band .purpose{font-family:"Montserrat",Arial,sans-serif;font-weight:600;color:var(--green-light);font-size:9.4px;margin-right:9px}
.footer-band .leaf{width:9px;height:9px;border-radius:50%;background:var(--green-light);margin-right:9px}
.footer-band .url{margin-left:auto;color:var(--green-light);font-weight:600}
</style>
</head>
<body>

<section class="outside">
  <div class="panel commitment">
    <h3 class="heading">OUR COMMITMENT</h3>
    <p>These Principles guide all of us working together to support communities before, during and long after disasters.</p>
    <p class="motto">Stronger together.<br>Recovering together.</p>
    <div class="art" role="img" aria-label="Illustration of a flowering eucalyptus branch with golden blossoms"></div>
  </div>

  <div class="panel partners">
    <h3 class="heading">PARTNERS IN RECOVERY</h3>
    <div class="logo-grid">
      <div class="logo-slot"></div><div class="logo-slot"></div><div class="logo-slot"></div>
      <div class="logo-slot"></div><div class="logo-slot"></div><div class="logo-slot"></div>
      <div class="logo-slot"></div><div class="logo-slot"></div><div class="logo-slot"></div>
      <div class="logo-slot"></div><div class="logo-slot"></div><div class="logo-slot"></div>
    </div>
    <p class="note">Working together across all sectors<br>to strengthen recovery for every community.</p>
    <div class="rule"></div>
    <p class="learn">Learn more</p>
    <p class="url">www.sgcr-renewal.org.au</p>
  </div>

  <div class="panel cover">
    <svg width="318" height="386" viewBox="0 0 318 386" aria-hidden="true">
      <defs>
        <linearGradient id="sunset" x1="0" y1="1" x2="1" y2="0">
          <stop offset="0" stop-color="#e0652f"/><stop offset="1" stop-color="#f0a83e"/>
        </linearGradient>
      </defs>
      <path d="M180,0 C250,50 250,150 318,200 L318,0Z" fill="#8aa64f"/>
      <path d="M0,386 L0,320 C90,290 190,300 240,240 C275,195 295,170 318,150 L318,386Z" fill="#f1e9d2"/>
      <path d="M0,386 L0,345 C100,318 205,320 255,255 C282,220 300,200 318,190 L318,386Z" fill="url(#sunset)"/>
    </svg>
    <div role="img" aria-label="Illustration of eucalyptus leaves and gum blossoms" style="position:absolute;left:190px;top:270px;width:120px;height:110px;border-radius:50%;background:radial-gradient(ellipse,rgba(12,59,75,.55),rgba(12,59,75,0) 70%)"></div>
    <p class="kicker heading">SHARED GUIDELINES FOR</p>
    <h1>Community<span>Renewal</span></h1>
    <p class="tagline">Guiding recovery.<br>Strengthening communities.<br>Building a resilient Australia.</p>
  </div>

  <div class="panel overview">
    <h3 class="heading">THE SHARED GUIDELINES<br>FOR COMMUNITY RENEWAL</h3>
    <p style="top:86px">The Shared Guidelines for Community Renewal provide a nationally agreed framework to guide recovery policy and practice across Australia.</p>
    <p style="top:134px">The Principles support recovery practitioners, governments, non-government organisations and communities to deliver effective, community-centred recovery outcomes.</p>
    <p style="top:196px">They reflect contemporary recovery practice and recognise that recovery is long-term, non-linear and unique to every community.</p>
    <div class="people" role="img" aria-label="Line illustration of a group of community members"></div>
    <p class="pledge">Recovery is about <em>people, connections and possibilities.</em> Together, we build stronger, more resilient communities.</p>
  </div>
</section>

<section class="inside">
  <div class="panel relationship">
    <h3 class="heading">THE RELATIONSHIP<br>BETWEEN THE PRINCIPLES</h3>
    <p style="top:56px">The six principles are interconnected and reinforce one another.</p>
    <p style="top:83px">Understanding context and recognising complexity are foundational to all recovery efforts.</p>
    <svg class="venn" width="169" height="220" viewBox="0 0 169 220" role="img" aria-label="Diagram of six overlapping principle circles around Recovery Principles">
      <g font-family="Montserrat,Arial,sans-serif" font-weight="700" font-size="6" fill="#fff" text-anchor="middle">
        <circle cx="98" cy="80" r="35" fill="#7b9a3d" opacity=".95"/>
        <circle cx="140" cy="118" r="35" fill="#136b6e" opacity=".92"/>
        <circle cx="123" cy="172" r="35" fill="#e0652f" opacity=".92"/>
        <circle cx="69" cy="172" r="35" fill="#eea03a" opacity=".92"/>
        <circle cx="55" cy="118" r="35" fill="#7a4f94" opacity=".92"/>
        <circle cx="97" cy="128" r="29" fill="#0c3b4b" stroke="#fff" stroke-width="1.5"/>
        <text x="98" y="66">UNDERSTANDING</text><text x="98" y="74">CONTEXT</text>
        <text x="148" y="116">RECOGNISING</text><text x="148" y="124">COMPLEXITY</text>
        <text x="130" y="176">COMMUNITY-</text><text x="130" y="184">CENTRED</text><text x="130" y="192">APPROACHES</text>
        <text x="60" y="180">CAPACITY</text><text x="60" y="188">BUILDING</text>
        <text x="42" y="121" font-size="5.6">COMMUNICATION</text>
        <text x="97" y="126" font-size="7" fill="#f0c255">RECOVERY</text><text x="97" y="135" font-size="7" fill="#f0c255">PRINCIPLES</text>
      </g>
    </svg>
  </div>

  <article class="panel principle context">
    <div class="icon" role="img" aria-label="Understanding context symbol"></div>
    <h2>UNDERSTANDING<br>CONTEXT</h2>
    <p class="lead">Successful recovery is based on an understanding of each community's unique history, values, strengths and aspirations.</p>
    <ul>
      <li>Acknowledge strengths and past experiences</li>
      <li>Appreciate risks and stressors</li>
      <li>Embrace diversity, equity and inclusion</li>
      <li>Support those at greater risk</li>
      <li>Respect connections to Country and environment</li>
      <li>Recognise long-term impacts beyond local boundaries</li>
    </ul>
  </article>

  <article class="panel principle complexity">
    <div class="icon" role="img" aria-label="Recognising complexity symbol"></div>
    <h2>RECOGNISING<br>COMPLEXITY</h2>
    <p class="lead">Recovery is responsive to the complex and evolving nature of disasters and their impacts.</p>
    <ul>
      <li>Impacts are varied and can be long lasting</li>
      <li>Information is limited and changes over time</li>
      <li>Needs and expectations evolve</li>
      <li>Flexible action is essential</li>
      <li>Different knowledge and values may create tension</li>
      <li>Support over time fosters hope and growth</li>
    </ul>
  </article>

  <article class="panel principle community">
    <div class="icon" role="img" aria-label="Community-centred approaches symbol"></div>
    <h2>COMMUNITY-CENTRED<br>APPROACHES</h2>
    <p class="lead">Recovery is centred on people and communities, empowering them to lead their own recovery.</p>
    <ul>
      <li>Enable active participation in recovery</li>
      <li>Recognise different needs at different times</li>
      <li>Build on local strengths and assets</li>
      <li>Foster collaboration and partnerships</li>
      <li>Shared responsibility drives better outcomes</li>
    </ul>
  </article>

  <article class="panel principle coordination">
    <div class="icon" role="img" aria-label="Coordination symbol"></div>
    <h2>COORDINATION</h2>
    <p class="lead">Recovery requires a planned, coordinated and adaptive approach across all sectors.</p>
    <ul>
      <li>Align activities and resources</li>
      <li>Base decisions on evidence and community input</li>
      <li>Stay flexible and adapt</li>
      <li>Work in partnership</li>
      <li>Monitor, learn and improve</li>
    </ul>
  </article>

  <article class="panel principle communication">
    <div class="icon" role="img" aria-label="Communication symbol"></div>
    <h2>COMMUNICATION</h2>
    <p class="lead">Effective communication builds trust, shares information and supports informed decisions.</p>
    <ul>
      <li>Communicate early, clearly and consistently</li>
      <li>Listen and act on feedback</li>
      <li>Use accessible and inclusive approaches</li>
      <li>Tailor messages to audience and context</li>
      <li>Build trusted relationships</li>
    </ul>
  </article>

  <article class="panel principle capacity">
    <div class="icon" role="img" aria-label="Capacity building symbol"></div>
    <h2>CAPACITY<br>BUILDING</h2>
    <p class="lead">Building capacity strengthens individuals, communities and organisations for the future.</p>
    <ul>
      <li>Support learning and skill development</li>
      <li>Strengthen local leadership</li>
      <li>Invest in systems and networks</li>
      <li>Build resilience and sustainability</li>
      <li>Prepare for future challenges together</li>
    </ul>
  </article>

  <svg class="waves" width="1178" height="58" viewBox="0 0 1178 58" aria-hidden="true" preserveAspectRatio="none">
    <path d="M0,40 C120,10 220,10 340,30 C420,44 470,20 560,18 C650,16 700,40 800,34 C880,28 930,8 1010,14 C1090,20 1130,10 1178,12 L1178,58 L0,58Z" fill="#9db35a" opacity=".55"/>
    <path d="M340,58 C400,30 460,14 540,16 C610,18 640,36 700,40 L700,58Z" fill="#136b6e" opacity=".7"/>
    <path d="M600,58 C650,30 690,10 760,18 C820,26 840,50 880,58Z" fill="#6aa6a6" opacity=".55"/>
    <path d="M830,58 C880,32 940,24 1000,34 C1040,40 1060,50 1080,58Z" fill="#7a4f94" opacity=".5"/>
    <path d="M1000,58 C1060,30 1120,14 1178,18 L1178,58Z" fill="#eea03a" opacity=".7"/>
    <path d="M0,58 C80,36 160,30 260,44 C300,50 330,54 350,58Z" fill="#7b9a3d" opacity=".6"/>
  </svg>

  <footer class="footer-band">
    <span class="leaf"></span>
    <span class="purpose">ONE SHARED PURPOSE</span>
    <span>Guided by shared principles.&nbsp;&nbsp; Working together.&nbsp;&nbsp; Building resilient communities for the future.</span>
    <span class="url">www.sgcr-renewal.org.au</span>
  </footer>
</section>

</body>
</html>
```